Vortelan d.o.o. needes a web site design

We are a company dealing with automatic doors, industrial doors, roller shutters, access control systems.
We would like to get a design which is clean and neat, and here are some sites which work with similar products. These designs are some we like, but of course, I am looking for a design which is unique. We usually use grey and red colours, which you can see on www.vortelan.ba .
The sites we like are:
http://www.plexawin.com/gb/
http://www.brunosteca.it/eng/
http://faswoodportamel.com/

You have to understand, that we have 4 different groups of products, which are main groups. I would like if those 4 groups somehow could be in different colours. (Maybe "zuvex" colours), in order to separate the groups in some way.

Attached you have web site structure.

If any questions, please contact me.
Edvin

Target Market(s)

Bosnian market. Aluminium and PVC doors and window market, Construction companies, Supermarkets-Retail, Gas stations, Banks, Food industry, Heavy industry.

Industry/Entity Type

It Company

Contact Information for Business Card

I have attached our current business card in PDF. I weould like english on one side, bosnian on other side.

Logo Text

Vortelan is the name of the company, our core business is automation!

Number of Pages Required

5+ page

Font styles to use
Sans Serif

Colors
ec1f27
0792cd
9bcb3c
ffc214
ffffff

```html
<!DOCTYPE html>
<html lang="bs">
<head>
<meta charset="utf-8">
<title>Vortelan d.o.o. – Rolo Vrata</title>
<link rel="stylesheet" href="https://fonts.googleapis.com/css2?family=Open+Sans:ital,wght@0,400;0,600;0,700;1,400;1,700;1,800&display=swap">
<style>
:root{
  --red:#e8606a;
  --red-dark:#d9414d;
  --red-soft:#eb9aa0;
  --blue:#0a8fcc;
  --blue-text:#1a8fcf;
  --grey:#c4c4c4;
  --grey-text:#5a5a5a;
  --white:#ffffff;
  --ink:#111111;
}
*{margin:0;padding:0;box-sizing:border-box}
html,body{width:1200px;height:960px;overflow:hidden}
body{position:relative;background:var(--white);font-family:"Open Sans",sans-serif;color:var(--ink)}
.abs{position:absolute}

.brand{left:53px;top:38px;display:flex;align-items:center;gap:14px}
.brand-mark{width:34px;height:34px;background:var(--red-dark)}
.brand-name{font-size:34px;font-weight:600;color:var(--grey-text);letter-spacing:1px}

.search{left:882px;top:17px;width:254px;height:27px;background:var(--red-soft);color:var(--white);font-size:14px;line-height:27px;padding-left:11px}

.main-nav{left:0;top:125px;width:1200px;height:27px;background:var(--red);border-bottom:2px solid #c9c9c9;box-shadow:0 2px 2px rgba(0,0,0,.15)}
.nav-item{position:absolute;top:0;height:27px;line-height:27px;font-size:14.5px;color:var(--white)}
.nav-item.active{background:var(--white);color:var(--blue);font-weight:700;padding:0 12px;left:621px;width:99px}

.dropdown{left:621px;top:148px;width:310px}
.dropdown-item{height:37px;line-height:37px;padding-left:16px;font-size:14.5px;color:var(--white);background:var(--blue);border-bottom:1px solid #d8eaf3}
.dropdown-item.current{background:var(--white);color:var(--blue);font-weight:700;height:39px;line-height:39px}

.breadcrumb{left:52px;top:162px;font-size:12px;font-style:italic}
.breadcrumb .here{color:var(--blue)}

.hero{left:0;top:187px;width:1200px;height:589px;background:linear-gradient(180deg,#cfe9f7 0%,#bfe1f4 45%,#d7eef9 100%)}

.page-title{left:53px;top:192px;font-size:50px;font-weight:800;font-style:italic;color:var(--blue);text-shadow:2px 2px 0 var(--white)}

.product-card{position:absolute;width:308px;height:230px;background:var(--white);box-shadow:1px 2px 4px rgba(0,0,0,.3)}
.product-photo{position:absolute;top:6px}
.product-name{position:absolute;left:0;width:100%;text-align:center;font-size:25px;font-weight:700;font-style:italic;color:var(--blue-text)}

.footer{left:0;top:776px;width:1200px;height:184px;background:var(--grey);color:var(--white);font-size:14px}
.contact-row{position:absolute;left:46px;display:flex}
.contact-row b{width:21px;font-weight:700}
.company-info{position:absolute;right:759px;top:52px;text-align:right;line-height:20.5px}
.quote-btn{left:802px;top:795px;width:332px;height:75px;background:var(--red);border:3px solid var(--white);border-radius:10px;box-shadow:1px 3px 4px rgba(0,0,0,.3);color:var(--white);font-size:37px;font-weight:700;font-style:italic;text-align:center;line-height:69px}
.copyright{right:67px;top:928px;color:var(--white);font-size:14px}
</style>
</head>
<body>

<div class="abs brand"><span class="brand-mark"></span><span class="brand-name">Vortelan d.o.o.</span></div>
<div class="abs search">Pretraga ovdje...</div>

<nav class="abs main-nav">
  <span class="nav-item" style="left:261px">Home</span>
  <span class="nav-item" style="left:327px">Automatska Vrata</span>
  <span class="nav-item" style="left:485px">Industrijska Vrata</span>
  <span class="nav-item active">Rolo Vrata</span>
  <span class="nav-item" style="left:734px">Kontrola Pristupa</span>
  <span class="nav-item" style="left:882px">Reference</span>
</nav>

<div class="abs breadcrumb">Home / Rolo Vrata / <span class="here">Spiralna brza rolo vrata</span></div>

<div class="abs hero" role="img" aria-label="Svijetloplava fotografija industrijske utovarne rampe s vratima"></div>

<ul class="abs dropdown" style="list-style:none">
  <li class="dropdown-item">Rolo rešetke</li>
  <li class="dropdown-item">Brzotekuća rolo PVC vrata</li>
  <li class="dropdown-item current">Spiralna brza rolo vrata</li>
</ul>

<h1 class="abs page-title">ROLO VRATA</h1>

<div class="product-card" style="left:53px;top:269px">
  <div class="product-photo" role="img" aria-label="Plava brza rolo vrata na fasadi hale" style="left:5px;width:298px;height:178px;background:linear-gradient(180deg,#3f7fd6,#1659c8 60%,#e6e6e6)"></div>
  <div class="product-name" style="top:187px">Vantroll 40</div>
</div>

<div class="product-card" style="left:442px;top:269px">
  <div class="product-photo" role="img" aria-label="Srebrna izolirana rolo vrata u skladištu" style="left:78px;width:150px;height:178px;background:linear-gradient(90deg,#8c8f8f,#c9cacb 50%,#a79a86)"></div>
  <div class="product-name" style="top:187px">Vantroll ISO</div>
</div>

<div class="product-card" style="left:830px;top:269px">
  <div class="product-photo" role="img" aria-label="Spiralna rolo vrata s perforiranim lamelama" style="left:4px;width:298px;height:179px;background:linear-gradient(90deg,#8a8166,#a8aaa9 30%,#9c9e9f)"></div>
  <div class="product-name" style="top:187px">Vantroll Airflow</div>
</div>

<div class="product-card" style="left:53px;top:527px">
  <div class="product-photo" role="img" aria-label="Dva prikaza sivih rolo vrata, zatvorena i otvorena" style="left:4px;top:15px;width:300px;height:163px;background:linear-gradient(90deg,#f2f2f2,#8d8c85 20%,#9a9992 50%,#8d8c85 80%,#f2f2f2)"></div>
  <div class="product-name" style="top:194px">Rolo Vrata</div>
</div>

<footer class="abs footer">
  <div class="contact-row" style="top:31px"><b>A</b><span>Lipova Aleja BB,<br>74000 BREZINA</span></div>
  <div class="contact-row" style="top:82px"><b>T</b><span>053/410-260</span></div>
  <div class="contact-row" style="top:102px"><b>F</b><span>053/410-261</span></div>
  <div class="contact-row" style="top:122px"><b>M</b><span>066/318-442</span></div>
  <div class="contact-row" style="top:142px"><b>E</b><span>info@vortelan.ba</span></div>
  <div class="company-info">PDV broj: 409175520031<br>ID broj: 4409175520031<br>Poslovna banka:<br>Kestral Bank Brezina<br>172-038-004-2290-015</div>
</footer>

<div class="abs quote-btn">Zatražiti Citat!</div>
<div class="abs copyright">C 2008-2016- Vortelan d.o.o Brezina</div>

</body>
</html>
```